Fundraising Brochure Design for Environmental Organization

We need a fundraising brochure designed for the Ashby and Tillard Streamwarden. This is an environmental group that helps keep the Ashby and Tillard rivers open to the public and clean for swimming and fishing. The brochure will be used to help raise money for the organization. The brochure text, layout and image options, are given. Also included are two examples of brochures we like. The layout should be clean (not cluttered), easy to read, and attractive to look at. It should communicate the beauty of the rivers and encourage people to get involved.
Updates

Hello Everyone, Thank you for submitting so many wonderful designs!! We are working with our client to review each one. Next week we will contact you with feedback from the client, and let you know if they have any requests for changes to the designs before making the final decision. Have a great weekend!

Hello Designers, Thank you for submitting such wonderful designs. We will be meeting soon to discuss the designs with our client. Once we get feedback from them we will be in touch. Thank you for your patience.

Target Market(s)

The target audience for this brochure includes people who are rich homeowners, over 60 years old, who may have a vacation home, have a high-paying job, may own their own business, may be a doctor, lawyer, etc., dive a luxury car, and owns a boat or airplane.

The target audience also includes people who travel a lot, may be retired, even at a young age, and also younger people who are wealthy through inheritance.

Industry/Entity Type

Group

Requirements
Must have
• Must be a tri-fold brochure matching the dimensions provided in the Brochure Interior and Exterior Dimensions files.
Each page must include the text provided in the Fundraising Brochure Text file.
The logos listed in the Fundraising Brochure Text file are provided and must be included in the brochure where indicated.
Should not have
• There should be no pictures of pools.
Not all of the photos provided should be used in the brochure.
Do not edit the text.

```html
<!DOCTYPE html>
<html lang="en">
<head>
<meta charset="utf-8">
<title>Ashby and Tillard Streamwarden – Inside Spread</title>
<link href="https://fonts.googleapis.com/css2?family=Ubuntu:wght@400;500&display=swap" rel="stylesheet">
<style>
  :root {
    --ink: #2a2c6b;
    --sky-top: #b9dcf4;
    --sky-low: #d9ecf8;
    --trees-dark: #3e4a24;
    --trees-warm: #8a6a2e;
    --water: #4f7fae;
    --water-deep: #2f5f8f;
    --frame: rgba(255,255,255,0.55);
    --strip: #e4e6ea;
    --badge: #8e99a8;
  }
  html, body { margin: 0; padding: 0; overflow: hidden; }
  body { width: 1200px; height: 849px; background: #ffffff; font-family: "Ubuntu", sans-serif; }
  .spread { position: relative; width: 1200px; height: 849px; overflow: hidden; }

  .scene {
    position: absolute; inset: 0;
    background: linear-gradient(180deg,
      var(--sky-top) 0%, var(--sky-low) 40%,
      #9a8a4a 44%, var(--trees-warm) 50%, var(--trees-dark) 60%, #4a5a2a 70%,
      #8f9a7a 72%, var(--water) 74%, var(--water-deep) 100%);
  }

  .panel-title {
    position: absolute;
    writing-mode: vertical-rl; transform: rotate(180deg);
    font-weight: 500; font-size: 30px; color: var(--ink);
    margin: 0; white-space: nowrap; line-height: 1;
  }
  .rule { position: absolute; width: 2px; background: var(--ink); }

  .panel-copy {
    position: absolute; margin: 0;
    font-size: 14px; line-height: 20px; color: var(--ink);
    text-align: justify; letter-spacing: 0.1px;
  }
  .panel-copy p { margin: 0; }
  .checklist { list-style: none; margin: 0; padding: 0 0 0 8px; text-align: left; }
  .checklist li { position: relative; padding-left: 18px; }
  .checklist svg { position: absolute; left: 0; top: 5px; }

  .photo-frame {
    position: absolute; border-radius: 14px; background: var(--frame);
  }
  .photo {
    position: absolute; border-radius: 8px;
  }
  .photo-planting { background: linear-gradient(180deg, #8fae6a 0%, #5f7f3a 45%, #7a6a3e 70%, #8a9a5a 100%); }
  .photo-map { background: linear-gradient(90deg, #d8dcc8 0%, #e4e2d4 45%, #8fc2e8 55%, #6aa9d9 100%); }

  .partner-strip {
    position: absolute; left: 0; top: 770px; width: 400px; height: 50px;
    background: var(--strip); display: flex; align-items: center; justify-content: space-around;
  }
  .partner-badge { width: 90px; height: 26px; border-radius: 4px; background: var(--badge); }
</style>
</head>
<body>
<main class="spread">
  <div class="scene" role="img" aria-label="Photograph of a wide river with autumn trees on the far shore and a red patrol boat with three people aboard"></div>

  <!-- Panel 1 -->
  <h2 class="panel-title" style="left:34px; top:25px; height:370px;">Beautiful rivers in peril</h2>
  <div class="rule" style="left:82px; top:18px; height:362px;"></div>
  <div class="panel-copy" style="left:91px; top:31px; width:289px;">
    <p>You love these rivers – that's why you're here. And you're troubled by the signs that show these waters are threatened by pollution, erosion and a changing climate. Crumbling shorelines, disappearing islands, water so clogged with silt and clouded with algae that no underwater grasses can grow to provide habitat for fish and crabs, and oysters are struggling to survive. The rivers teem with bacteria after every rain.</p>
    <p>These rivers need help, and that's why there's a Streamwarden. We share your passion -- and your concern. For the past decade, we've been the only citizen environmental organization solely dedicated to protecting and restoring the Ashby and Tillard Rivers, one creek at a time.</p>
  </div>
  <div class="photo-frame" style="left:85px; top:383px; width:293px; height:355px;"></div>
  <div class="photo photo-planting" style="left:95px; top:392px; width:272px; height:335px;" role="img" aria-label="Photograph of volunteers kneeling to plant a young tree in a field"></div>

  <!-- Panel 2 -->
  <h2 class="panel-title" style="left:430px; top:25px; height:390px;">How we protect our rivers</h2>
  <div class="rule" style="left:477px; top:0; height:415px;"></div>
  <div class="panel-copy" style="left:497px; top:31px; width:284px;">
    <p>We work to make these rivers safe for swimming, fishing and wildlife by leveraging your donation with grants from public and private sources to:</p>
    <ul class="checklist">
      <li><svg width="11" height="10" viewBox="0 0 11 10"><path d="M1 5l3 3 6-7" fill="none" stroke="var(--ink)" stroke-width="1.6"/></svg>advocate for better environmental policies,</li>
      <li><svg width="11" height="10" viewBox="0 0 11 10"><path d="M1 5l3 3 6-7" fill="none" stroke="var(--ink)" stroke-width="1.6"/></svg>enforce environmental law,</li>
      <li><svg width="11" height="10" viewBox="0 0 11 10"><path d="M1 5l3 3 6-7" fill="none" stroke="var(--ink)" stroke-width="1.6"/></svg>monitor water quality,</li>
      <li><svg width="11" height="10" viewBox="0 0 11 10"><path d="M1 5l3 3 6-7" fill="none" stroke="var(--ink)" stroke-width="1.6"/></svg>expand public access to the water,</li>
      <li><svg width="11" height="10" viewBox="0 0 11 10"><path d="M1 5l3 3 6-7" fill="none" stroke="var(--ink)" stroke-width="1.6"/></svg>provide pump-out service to recreational boaters,</li>
      <li><svg width="11" height="10" viewBox="0 0 11 10"><path d="M1 5l3 3 6-7" fill="none" stroke="var(--ink)" stroke-width="1.6"/></svg>restore marshes and streambeds,</li>
      <li><svg width="11" height="10" viewBox="0 0 11 10"><path d="M1 5l3 3 6-7" fill="none" stroke="var(--ink)" stroke-width="1.6"/></svg>and create new forest buffers, wetlands and living shorelines that promote healthy waterways and stop pollution.</li>
    </ul>
  </div>

  <!-- Panel 3 -->
  <h2 class="panel-title" style="left:825px; top:25px; height:182px;">Who we are</h2>
  <div class="rule" style="left:872px; top:0; height:210px;"></div>
  <div class="panel-copy" style="left:887px; top:31px; width:280px;">
    <p>The Streamwarden serves as a voice for the rivers, working with local community groups and regional, national and international coalitions of environmental organizations to promote sensible legislation and responsible enforcement of existing laws that reduce pollution and improve water quality, advocating at the county, state and federal level.</p>
  </div>
  <div class="photo-frame" style="left:877px; top:218px; width:290px; height:194px;"></div>
  <div class="photo photo-map" style="left:885px; top:228px; width:270px; height:174px;" role="img" aria-label="Map of the bay region marking the location of the Ashby and Tillard rivers"></div>

  <!-- Partners -->
  <div class="partner-strip" aria-label="Partner organizations">
    <div class="partner-badge"></div>
    <div class="partner-badge"></div>
    <div class="partner-badge"></div>
  </div>
</main>
</body>
</html>
```